Home Page Design for Motor Manufacturer

Hello,
please design the homepage for a manufacturer of industry motors. I am looking for a professional, clean and minimalistic design. Since this a rather conservative industry it should get a professional look but since it is a redesign there should be some modern that gives is the modern touch of innovation.
A competitor's homepage I like is:
https://www.valtrosk.com/en/
What I like about this website:
* clean, minimal, well structured design
* mega menu
For this project please find attached the wireframes (most buttons are in German but by context and Google translate you will easily figure it out; only unclear - "Messe" means "trade exhibition"). The paddings and margins are NOT exact. Also any color of backgrounds etc. chosen is not meant to represent a real color but rather to illustrate the object and maybe show there should be some background emphasis (color or image).
Wireframes:
https: //www.filmavek. com / t / pxuTQmD7ZJHaLrwY
In both wireframes the only thing that is different is the Service section. I expect from the winner both designs for this service section: one with normal cart design and one with tabs as filters to search products (find image for product categories attached)
In the header use on the left the following text:
h1: "Your competent partner for industrial engines,
-transmission and drawing parts
with more than 5000 satisfied customers "
primary button: Our products
sec. button: Download catalog
and on the right side we feature one or more product images (like putting them in a nice display together).
I also think of a solid background color or subtle gradient for the hero section.
The winner should also design an open mega menu version.
Menu items in this order:
• Home page
• Gearboxes & Motors
• Engine components
• Drawing parts
• Machines & accessories
• About us
• Contact
Also create a language switch with globe symbol and DE for Germany and EN for English above the nav plus the telephone number with icon (user dummy number +49 (0) 987654321)
Output should be in Figma, Sketch or PSD.
Fonts + color to use:
header: Proza Libre, bold, # 0171A1
body: Open Sans, regular, black
Primary accent color: # 0171A1
Text black or dark gray
background: light gray, white or shade of blue
More image resources:
https://www.filmavek.com/t/QrnLVdHZPKEX1bmu
If there are any questions please do not hesitate to ask.
Target Market(s)
B2B - anyone with industrial machinery needing small motors (not car engines)
Industry/Entity Type
Manufacturing
Number of Pages Required
1 page
Requirements
Must have
- see above
Nice to have
- see above
Should not have
- see above

```html
<!DOCTYPE html>
<html lang="en">
<head>
<meta charset="utf-8">
<title>KVM – Industrial Engines</title>
<link href="https://fonts.googleapis.com/css2?family=Proza+Libre:wght@500;600;700&family=Open+Sans:wght@400;600;700&display=swap" rel="stylesheet">
<style>
:root{
  --accent:#0171a1;
  --accent-dark:#015a82;
  --navy:#0d4f74;
  --ink:#1e1e1e;
  --gray:#555b61;
  --light:#f4f4f4;
  --topbar:#eceef1;
  --footer:#1d2235;
  --pale-blue:#dce8ef;
  --white:#ffffff;
}
*{box-sizing:border-box;margin:0;padding:0}
html,body{width:1200px;height:4386px;overflow:hidden}
body{position:relative;font-family:"Open Sans",sans-serif;color:var(--ink);background:var(--white)}
.abs{position:absolute}
h1,h2,h3{font-family:"Proza Libre",sans-serif;font-weight:600}
.btn{position:absolute;display:flex;align-items:center;justify-content:center;font-family:"Proza Libre",sans-serif;font-size:17px;color:var(--white);background:var(--accent)}
.btn.dark{background:var(--navy)}
.btn.pill{border-radius:24px}

/* top bar */
.topbar{position:absolute;left:0;top:0;width:1200px;height:72px;background:var(--topbar)}
.brand{position:absolute;font-family:"Proza Libre",sans-serif;font-weight:700;color:var(--accent);letter-spacing:2px}
.topbar .brand{left:121px;top:10px;font-size:42px;line-height:52px}
.top-phone{position:absolute;left:822px;top:25px;display:flex;align-items:center;gap:8px;font-size:14px;color:var(--accent)}
.lang{position:absolute;left:1014px;top:22px;width:66px;height:30px;border:1px solid #d3d6da;background:var(--white);font-size:13px;color:#777;display:flex;align-items:center;padding-left:12px;gap:12px}
.caret{width:0;height:0;border-left:5px solid transparent;border-right:5px solid transparent;border-top:5px solid #999}

/* nav */
.nav{position:absolute;left:0;top:72px;width:1200px;height:56px;background:var(--white);border-bottom:1px solid #dcdfe2}
.nav a{position:absolute;top:18px;font-size:15px;color:#2d3338;text-decoration:none;display:flex;align-items:center;gap:7px}
.nav a.active{color:var(--accent)}
.nav .caret{border-top-color:#888;border-width:4px 4px 0}

/* hero */
.hero{position:absolute;left:0;top:128px;width:1200px;height:625px;overflow:hidden}
.hero h1{position:absolute;left:121px;top:170px;font-size:37px;line-height:51px;color:var(--white);font-weight:700}
.hero p{position:absolute;left:121px;top:296px;font-family:"Proza Libre",sans-serif;font-size:21px;line-height:35px;color:var(--white)}
.hero .btn{top:391px;height:43px}
.btn.outline{background:transparent;border:2px solid var(--white)}

/* why */
.section-title{position:absolute;left:0;width:1200px;text-align:center;font-size:44px;color:var(--ink);font-weight:500}
.lead{position:absolute;left:0;width:1200px;text-align:center;font-size:15.5px;line-height:27px;color:var(--ink)}
.feature{position:absolute;top:1016px;height:206px;background:#f2f2f2;display:flex;flex-direction:column;align-items:center;justify-content:center;gap:18px;font-family:"Proza Libre",sans-serif;font-size:20px}
.feature.active{top:984px;height:270px;background:var(--accent);color:var(--white);box-shadow:0 6px 14px rgba(0,0,0,.25);gap:12px;padding:0 30px;text-align:center}
.feature.active small{font-family:"Open Sans",sans-serif;font-size:13px;line-height:24px}

/* products */
.products{position:absolute;left:0;top:1399px;width:1200px;height:868px;background:linear-gradient(135deg,#2c3136 0%,#4a4f57 35%,#6e5a48 60%,#3b4654 80%,#30353c 100%)}
.products .section-title{color:var(--white);top:60px}
.pcard{position:absolute;width:300px;height:255px;background:var(--white);text-align:center;font-family:"Proza Libre",sans-serif;font-size:19px}
.pcard.blue{background:var(--accent);color:var(--white)}
.pcard .shot{position:absolute;left:85px;top:20px;width:130px;height:130px;border-radius:10px;background:radial-gradient(circle at 40% 40%,#e8ebee,#8e959c 70%,#3a3f45)}
.pcard .name{position:absolute;left:0;top:178px;width:100%}
.pill-tag{position:absolute;left:100px;bottom:-14px;width:108px;height:28px;border-radius:14px;background:#8a8f94;color:var(--white);font-family:"Open Sans",sans-serif;font-size:14px;display:flex;align-items:center;justify-content:center}
.pcard.blue .pill-tag{background:#2b2f34}

/* trade */
.tcard{position:absolute;top:2473px;width:298px;height:398px;background:#f4f4f4}
.tcard .photo{position:absolute;left:0;width:298px;height:199px;background:linear-gradient(160deg,#2d4a7a,#5f86b8 45%,#c9c2b4 75%,#3a3f4a)}
.tcard .body{position:absolute;left:29px;width:245px}
.tcard h3{font-family:"Open Sans",sans-serif;font-weight:400;font-size:17px;margin-bottom:14px}
.tcard p{font-size:13px;line-height:24px;color:var(--gray)}
.tcard .actions{display:flex;gap:6px;margin-top:14px}
.tcard .actions span{height:32px;padding:0 17px;display:flex;align-items:center;font-size:15px;color:var(--white);background:var(--accent)}
.tcard .actions span.dark{background:var(--navy);padding:0 24px}

/* about */
.about{position:absolute;left:0;top:3077px;width:1200px;height:587px;background:var(--light)}
.about .frame{position:absolute;left:157px;top:119px;width:342px;height:365px;border:6px solid var(--accent)}
.about .photo{position:absolute;left:121px;top:84px;width:344px;height:366px;background:linear-gradient(150deg,#5b6d7d,#c8a348 45%,#4e5a63 75%,#2d3338)}
.about h2{position:absolute;left:575px;top:88px;font-size:40px;font-weight:500}
.about .intro{position:absolute;left:575px;top:154px;width:480px;font-size:17px;line-height:27px;font-weight:600}
.about .text{position:absolute;left:575px;top:226px;width:480px;font-size:14.5px;line-height:25.5px;color:var(--gray)}

/* download */
.download{position:absolute;left:0;top:3664px;width:1200px;height:268px;background:var(--pale-blue);overflow:hidden}
.download h2{position:absolute;right:645px;top:40px;font-size:38px;font-weight:500}
.download p{position:absolute;right:645px;top:102px;font-size:17.5px;line-height:31px;text-align:right;width:420px}
.catalog-art{position:absolute;left:620px;top:30px;width:490px;height:210px;border-radius:8px;background:radial-gradient(ellipse at 45% 50%,#c3d5e1 0%,#d2e0ea 45%,var(--pale-blue) 80%)}

/* contact strip */
.contact{position:absolute;left:0;top:3932px;width:1200px;height:170px;background:var(--white)}
.citem{position:absolute;top:50px;display:flex;align-items:center;gap:14px}
.citem .label{font-size:13px;font-weight:600;margin-bottom:4px}
.citem .val{font-size:13px;color:#333;line-height:18px}
.citem .val.big{font-size:18px;color:var(--accent);font-weight:600}
.divider{position:absolute;top:30px;width:1px;height:92px;background:#cfd5da}

/* footer */
.footer{position:absolute;left:0;top:4102px;width:1200px;height:284px;background:var(--footer);color:#c6cad3}
.footer .brand{left:121px;top:30px;font-size:50px;line-height:60px;color:var(--white)}
.footer h4{position:absolute;font-family:"Open Sans",sans-serif;font-weight:400;font-size:16px;color:var(--white)}
.footer ul{position:absolute;list-style:none;font-size:14px;line-height:24px}
.news{position:absolute;left:121px;top:128px;font-size:14px;color:var(--white)}
.news-form{position:absolute;left:121px;top:156px;width:268px;height:34px;border-radius:17px;background:var(--white);overflow:hidden;display:flex}
.news-form span{flex:1;font-size:12px;color:#888;padding:9px 0 0 20px}
.news-form b{width:100px;background:var(--accent);color:var(--white);font-weight:400;font-size:14px;display:flex;align-items:center;justify-content:center}
.legal{position:absolute;top:4337px;font-size:13.5px;color:#c6cad3}
</style>
</head>
<body>

<header>
  <div class="topbar">
    <div class="brand">KVM</div>
    <div class="top-phone">
      <svg width="22" height="18" viewBox="0 0 24 20" fill="none" stroke="currentColor" stroke-width="1.6"><path d="M4 2c-2 1-2 4 1 8s7 8 10 8c2 0 3-1 3-2l-3-3-2 1c-2-1-4-3-5-5l1-2-3-3z"/><path d="M14 3a6 6 0 0 1 6 6M14 6a3 3 0 0 1 3 3"/></svg>
      +49 (0) 987654321
    </div>
    <div class="lang">EN <span class="caret"></span></div>
  </div>
  <nav class="nav">
    <a class="active" style="left:119px">Home</a>
    <a style="left:192px">Gearboxes &amp; Motors <span class="caret"></span></a>
    <a style="left:385px">Engine Components <span class="caret"></span></a>
    <a style="left:574px">Drawing parts <span class="caret"></span></a>
    <a style="left:718px">Machines &amp; Accessories <span class="caret"></span></a>
    <a style="left:931px">About Us</a>
    <a style="left:1026px">Contact</a>
  </nav>
</header>

<section class="hero">
  <svg class="abs" style="left:0;top:0" width="1200" height="625" viewBox="0 0 1200 625">
    <defs><linearGradient id="heroBg" x1="0" y1="0" x2="1" y2="1"><stop offset="0" stop-color="#0a6d9b"/><stop offset="1" stop-color="#015f8a"/></linearGradient></defs>
    <path d="M0 0H1200V510C900 560 500 520 0 620Z" fill="url(#heroBg)"/>
    <path d="M300 0C500 120 700 60 1000 180" stroke="#ffffff" stroke-opacity=".06" stroke-width="60" fill="none"/>
    <circle cx="830" cy="414" r="188" fill="none" stroke="#1d9fd2" stroke-width="10"/>
    <circle cx="830" cy="414" r="176" fill="#ffffff"/>
    <path d="M1049 154l9-8 9 8" stroke="#ffffff" stroke-opacity=".6" stroke-width="2" fill="none"/>
    <circle cx="1059" cy="214" r="28" fill="#ffffff" stroke="#4fb3dc" stroke-width="3"/>
    <circle cx="1059" cy="292" r="33" fill="#ffffff" stroke="#4fb3dc" stroke-width="5"/>
    <circle cx="1059" cy="371" r="28" fill="#ffffff" stroke="#4fb3dc" stroke-width="3"/>
  </svg>
  <div class="abs" role="img" aria-label="Silver planetary gearbox with blue label" style="left:690px;top:305px;width:290px;height:200px;border-radius:40px;background:linear-gradient(120deg,#d9dde1,#8b929a 45%,#1d2a3a 70%,#1b7fc0)"></div>
  <div class="abs" role="img" aria-label="Gearbox thumbnail" style="left:1041px;top:196px;width:36px;height:36px;border-radius:50%;background:linear-gradient(135deg,#c9ced3,#3d4650)"></div>
  <div class="abs" role="img" aria-label="Gear motor thumbnail" style="left:1038px;top:271px;width:42px;height:42px;border-radius:50%;background:linear-gradient(135deg,#c9ced3,#1b7fc0 60%,#1d2a3a)"></div>
  <div class="abs" role="img" aria-label="Electric motor thumbnail" style="left:1041px;top:353px;width:36px;height:36px;border-radius:50%;background:linear-gradient(135deg,#2f5e8a,#1d2a3a)"></div>
  <h1>Your Competent Partner<br>For Industrial Engines</h1>
  <p>Transmission And Drawing Parts<br>With More Than 5000 Satisfied Customers</p>
  <div class="btn pill dark" style="left:121px;width:155px">Learn More</div>
  <div class="btn pill outline" style="left:289px;width:155px">All Porducts</div>
</section>

<section class="why">
  <h2 class="section-title" style="top:808px">Why Choose Us</h2>
  <p class="lead" style="top:884px">Lorem Ipsum is simply dummy text of the printing and typesetting industry. Lorem Ipsum has been<br>the industry's standard dummy text ever since the 1500s Lorem Ipsum is simply dummy</p>
  <div class="feature" style="left:0;width:283px">
    <svg width="80" height="80" viewBox="0 0 80 80" fill="none" stroke="#0171a1" stroke-width="5"><circle cx="40" cy="20" r="12"/><path d="M20 48c4-10 36-10 40 0"/><g fill="#0171a1" stroke="none"><path d="M14 52l3 7 7 1-5 5 1 7-6-3-6 3 1-7-5-5 7-1z"/><path d="M40 52l3 7 7 1-5 5 1 7-6-3-6 3 1-7-5-5 7-1z"/><path d="M66 52l3 7 7 1-5 5 1 7-6-3-6 3 1-7-5-5 7-1z"/></g></svg>
    Customer Satisfaction
  </div>
  <div class="feature active" style="left:300px;width:299px">
    <svg width="54" height="54" viewBox="0 0 54 54" fill="none" stroke="#fff" stroke-width="3"><circle cx="27" cy="27" r="24" stroke-dasharray="6 3"/><circle cx="27" cy="27" r="17"/><path d="M32 20c-2-2-9-2-9 2s9 3 9 7-7 4-9 2M27 15v24"/></svg>
    <span>Optimal Price</span>
    <small>Lorem Ipsum is simply dummy text of the printing and typesetting industry. Lorem Ipsum has been.</small>
    <svg width="28" height="28" viewBox="0 0 28 28" fill="none" stroke="#fff" stroke-width="2"><circle cx="14" cy="14" r="12"/><path d="M9 12l5 5 5-5"/></svg>
  </div>
  <div class="feature" style="left:618px;width:281px">
    <svg width="80" height="80" viewBox="0 0 80 80" fill="#0171a1"><circle cx="26" cy="38" r="16"/><circle cx="26" cy="38" r="6" fill="#f2f2f2"/><circle cx="56" cy="20" r="11"/><circle cx="56" cy="20" r="4" fill="#f2f2f2"/><circle cx="58" cy="56" r="11"/><circle cx="58" cy="56" r="4" fill="#f2f2f2"/></svg>
    Smooth Implementation
  </div>
  <div class="feature" style="left:916px;width:284px">
    <svg width="80" height="80" viewBox="0 0 80 80" fill="#0171a1"><path d="M22 48L12 76l14-6 8 10 6-22zM58 48l10 28-14-6-8 10-6-22z"/><circle cx="40" cy="32" r="26"/><circle cx="40" cy="32" r="18" fill="#f2f2f2"/><path d="M40 19l4 8 9 1-7 6 2 9-8-5-8 5 2-9-7-6 9-1z"/></svg>
    High Quality
  </div>
</section>

<section class="products">
  <h2 class="section-title">Our Products</h2>
  <div class="pcard blue" style="left:451px;top:160px">
    <div class="shot" role="img" aria-label="Right-angle gearbox"></div>
    <div class="name">Product Category</div>
    <div class="pill-tag">Details</div>
  </div>
  <div class="pcard" style="left:129px;top:300px">
    <div class="shot" role="img" aria-label="Planetary gearbox"></div>
    <div class="name">Product Category</div>
    <div class="pill-tag">Details</div>
  </div>
  <div class="pcard" style="left:771px;top:300px">
    <div class="shot" role="img" aria-label="Electric gear motor"></div>
    <div class="name">Product Category</div>
    <div class="pill-tag">Details</div>
  </div>
  <div class="pcard" style="left:451px;top:453px">
    <div class="shot" role="img" aria-label="Harmonic drive component"></div>
    <div class="name">Product Category</div>
    <div class="pill-tag">Details</div>
  </div>
  <div class="btn dark" style="left:524px;top:766px;width:152px;height:44px">View More</div>
</section>

<section class="trade">
  <h2 class="section-title" style="top:2378px">Trade Exhibition</h2>
  <div class="tcard" style="left:119px">
    <div class="photo" style="top:0" role="img" aria-label="Crowded trade fair hall"></div>
    <div class="body" style="top:222px"><h3>Trade Exhibition</h3><p>Lorem Ipsum is simply dummy text of the printing and typesetting industry.</p><div class="actions"><span>Free tickets</span><span class="dark">Details</span></div></div>
  </div>
  <div class="tcard" style="left:451px">
    <div class="body" style="top:25px"><h3>Trade Exhibition</h3><p>Lorem Ipsum is simply dummy text of the printing and typesetting industry.</p><div class="actions"><span>Free tickets</span><span class="dark">Details</span></div></div>
    <div class="photo" style="top:199px" role="img" aria-label="Visitors walking through an exhibition hall"></div>
  </div>
  <div class="tcard" style="left:781px">
    <div class="photo" style="top:0;background:linear-gradient(160deg,#3c4450,#8fa4b3 45%,#a9c9a0 70%,#2f3640)" role="img" aria-label="Exhibition booths in a hall"></div>
    <div class="body" style="top:222px"><h3>Trade Exhibition</h3><p>Lorem Ipsum is simply dummy text of the printing and typesetting industry.</p><div class="actions"><span>Free tickets</span><span class="dark">Details</span></div></div>
  </div>
  <div class="btn dark" style="left:524px;top:2921px;width:152px;height:47px">View More</div>
</section>

<section class="about">
  <div class="frame"></div>
  <div class="photo" role="img" aria-label="Worker in a hard hat operating a lathe"></div>
  <h2>About Us</h2>
  <p class="intro">Lorem Ipsum is simply dummy text of the printing and typesetting industry.</p>
  <p class="text">Lorem Ipsum has been the industry's standard dummy text ever since the 1500 Lorem Ipsum is simply dummy text of the printing and typesetting industry. Lorem Ipsum has been the industry's standard dummy text ever since the 1500s. Lorem Ipsum is simply dummy text of the printing and typesetting industry. Lorem Ipsum has been the industry's standard dummy text ever since the 1500s. Lorem Ipsum is simply dummy text of the printing.</p>
  <div class="btn" style="left:577px;top:429px;width:151px;height:48px">Learn More</div>
</section>

<section class="download">
  <div class="catalog-art" role="img" aria-label="Catalog download illustration: document with arrow inside a circle among soft bubbles"></div>
  <h2>Download Catalog</h2>
  <p>Lorem Ipsum is simply dummy text of the printing and typesetting industry</p>
  <div class="btn pill" style="left:373px;top:177px;width:182px;height:43px">Download Now</div>
</section>

<section class="contact">
  <div class="citem" style="left:168px">
    <svg width="46" height="46" viewBox="0 0 46 46" fill="none" stroke="#0171a1" stroke-width="1.8"><path d="M8 6c-4 2-4 8 2 16s14 16 20 16c4 0 6-2 6-4l-6-6-4 2c-4-2-8-6-10-10l2-4-6-6z"/><path d="M26 6a14 14 0 0 1 14 14M26 12a8 8 0 0 1 8 8"/></svg>
    <div><div class="label">CALL Now</div><div class="val big">+49 (0) 987654321</div></div>
  </div>
  <div class="divider" style="left:436px"></div>
  <div class="citem" style="left:524px">
    <svg width="46" height="46" viewBox="0 0 46 46" fill="none" stroke="#0171a1" stroke-width="1.8"><path d="M23 38S12 24 12 16a11 11 0 0 1 22 0c0 8-11 22-11 22z"/><circle cx="23" cy="16" r="5"/><path d="M6 34c0 4 8 8 17 8s17-4 17-8"/></svg>
    <div><div class="label">ADDRESS</div><div class="val">Address, Lorem<br>Ipsum is simply</div></div>
  </div>
  <div class="divider" style="left:751px"></div>
  <div class="citem" style="left:832px">
    <svg width="46" height="46" viewBox="0 0 46 46" fill="none" stroke="#0171a1" stroke-width="1.8"><rect x="4" y="14" width="36" height="26"/><path d="M4 14l18 14 18-14M4 40l13-12M40 40l-13-12"/><path d="M14 14V6h16l6 6v8"/></svg>
    <div><div class="label">E-MAIL</div><div class="val">info@kvmdrive.com</div></div>
  </div>
</section>

<footer class="footer">
  <div class="brand">KVM</div>
  <div class="news">Subscribe to our newsletter</div>
  <div class="news-form"><span>Email address</span><b>Subscribe</b></div>
  <h4 style="left:450px;top:36px">Quick Links</h4>
  <ul style="left:450px;top:72px"><li>Home</li><li>Gearboxes &amp; Motors</li><li>Engine Components</li><li>Drawing Parts</li><li>Machines &amp; Accessories</li></ul>
  <h4 style="left:670px;top:36px">Category</h4>
  <ul style="left:670px;top:72px"><li>Category Name</li><li>Category Name</li><li>Category Name</li><li>Category Name</li><li>Category Name</li></ul>
  <h4 style="left:857px;top:36px">Stil have questions?</h4>
  <p class="abs" style="left:857px;top:74px;font-size:14px;line-height:22px">A representative will aswer your<br>questions as soon as possible.</p>
  <div class="btn" style="left:857px;top:142px;width:178px;height:42px;font-family:'Open Sans',sans-serif;font-size:15px;border-radius:21px 0 0 21px;justify-content:flex-end;padding-right:22px">Contact Now</div>
  <svg class="abs" style="left:859px;top:144px" width="38" height="38" viewBox="0 0 38 38" fill="none"><circle cx="19" cy="19" r="17" fill="#0171a1" stroke="#fff" stroke-width="1.5"/><path d="M12 11c-2 1-2 4 1 8s7 8 10 8c2 0 3-1 3-2l-3-3-2 1c-2-1-4-3-5-5l1-2-3-3z" stroke="#fff" stroke-width="1.4"/></svg>
</footer>
<div class="legal" style="left:132px">Copyright 2020 Kvm. All Rights Reserved.</div>
<div class="legal" style="left:851px">Privacy Policy &nbsp;&nbsp;|&nbsp;&nbsp; Terms Of Services</div>

</body>
</html>
```